Crestline Slate & Tile Needs a Business Card

Attached you will find your logo, my photo and design guidelines for a new business card. The final design will need two separate files to create an embossed card. The cards will be printed by www.plinkprint.com (Instructions below)
Format is the Zib SQUARE card
Crestline Slate And Tile is a brick and mortar, retail stone and tile shop.
One the front:
Crestline Slate And Tile
Gerald Finchcombe
Owner
48207 Vesper Hollow Blvd
Suite R & T
Charlotte, NC 28953
Cell: 704-555-0183
Web: www.CrestlineSlateAndTile.com
(Make each word of the domain a different or alternating color)
On the back;
Something that shows beautiful colorful tile
Follow the design guide closely please. For more information see this page that describes creating the spot gloss file: https://www.plinkprint.com/us/business-cards/design-guidelines-spot-gloss
The logo is what we would like to have raised spot glossed.
Format is the Zib SQUARE card. See attahced guidlines.

```html
<!DOCTYPE html>
<html lang="en">
<head>
<meta charset="utf-8">
<title>Crestline Slate &amp; Tile — Business Card</title>
<link rel="stylesheet" href="https://fonts.googleapis.com/css2?family=Cormorant+Garamond:wght@600&family=Open+Sans:wght@400&display=swap">
<style>
  :root {
    --backdrop: #b7b7b7;
    --navy: #22323c;
    --paper: #ffffff;
    --ink: #1f2a32;
    --ochre: #a0651e;
    --rust: #a23a1e;
    --pattern-navy: #263744;
    --pattern-warm: #8c6a45;
    --photo-tone: #c3b7a6;
  }
  * { margin: 0; padding: 0; box-sizing: border-box; }
  html, body {
    width: 1200px; height: 995px; overflow: hidden;
    background: var(--backdrop);
  }
  .card {
    position: absolute; top: 296px;
    width: 401px; height: 402px;
  }
  .card--back { left: 192px; background: var(--navy); }
  .card--front { left: 607px; background: var(--paper); }

  .brand-name {
    font-family: "Cormorant Garamond", Georgia, serif;
    font-weight: 600;
    text-transform: uppercase;
    line-height: 1.1;
  }
  .card--back .brand-name {
    position: absolute; left: 0; right: 0; top: 168px;
    text-align: center; color: var(--paper);
    font-size: 30px; letter-spacing: 5px;
  }
  .card--front .brand-name {
    position: absolute; left: 169px; width: 214px; top: 60px;
    text-align: center; color: var(--ink);
    font-size: 27px; letter-spacing: 4px;
  }

  .tile-band {
    position: absolute; left: 55px; top: 0;
    width: 93px; height: 402px;
    background: linear-gradient(180deg, var(--pattern-navy), var(--pattern-warm) 50%, var(--pattern-navy));
  }
  .portrait {
    position: absolute; left: 38px; top: 135px;
    width: 129px; height: 133px; border-radius: 12px;
    background: linear-gradient(180deg, var(--photo-tone), #9c8f80);
  }

  .details {
    position: absolute; left: 174px; top: 0;
    font-family: "Open Sans", Arial, sans-serif;
    color: var(--ink);
  }
  .person-name {
    position: absolute; top: 146px; white-space: nowrap;
    font-family: "Cormorant Garamond", Georgia, serif;
    font-weight: 600; font-size: 20px; letter-spacing: 0.5px;
    text-transform: uppercase; color: var(--ink);
  }
  .role {
    position: absolute; top: 173px; white-space: nowrap;
    font-size: 14.5px; color: var(--ochre);
  }
  .rule {
    position: absolute; top: 202px; left: 2px;
    width: 26px; height: 1.5px; background: var(--ink);
  }
  .contact {
    position: absolute; top: 207px; white-space: nowrap;
    font-size: 14.5px; line-height: 21px;
  }
  .web { font-size: 13.6px; letter-spacing: -0.2px; }
  .web .domain { color: var(--rust); }
  .web .tld { color: var(--ochre); }
  .address {
    position: absolute; top: 296px; white-space: nowrap;
    font-size: 14.5px; line-height: 21.5px;
  }
</style>
</head>
<body>
  <section class="card card--back">
    <h1 class="brand-name">Crestline<br>Slate &amp; Tile</h1>
  </section>

  <section class="card card--front">
    <div class="tile-band" role="img" aria-label="Vertical band of colourful geometric mosaic tile pattern"></div>
    <div class="portrait" role="img" aria-label="Portrait photo of Gerald Finchcombe"></div>
    <h2 class="brand-name">Crestline<br>Slate &amp; Tile</h2>
    <div class="details">
      <p class="person-name">Gerald Finchcombe</p>
      <p class="role">Owner</p>
      <div class="rule"></div>
      <p class="contact">704-555-0183<br><span class="web">www.<span class="domain">CrestlineSlateAndTile</span><span class="tld">.com</span></span></p>
      <p class="address">48207 Vesper Hollow Blvd,<br>Suite R &amp; T<br>Charlotte, NC 28953</p>
    </div>
  </section>
</body>
</html>
```